Website design for staffing/workforce solutions company - Harbor Crest Solutions

Create a launch-ready website
Harbor Crest Solutions also known as HCS. This is a company that specializes in Staffing/Work force solutions for Healthcare/IT/Logistics/Maintenance/Construction/Manufacturing/Industrial/General Labor. HCS works with government agencies/contracts also. Use the attached logo in the build of the website. Website should be clean, modern, engaging, innovative. Website needs to speak to the professional services industry.
Harbor Crest Solutions or HCS is a certified VOSB, SDVOSB, DBE and Minority-Owned Business.
The website needs to be compliant for government contracting.

Website needs to include the following--
Modern UI/UX Enhancements: A hero section with a strong call-to-action.
Government Contracting Compliance: Certification display and a Capability Statement download.
Advanced Careers Section: A dedicated job application portal.
Social Media & Lead Generation: Links to Workvine, Quillo, and Pagebloom.
Security & Performance: Optimized for SEO, fast loading, and mobile responsiveness.
1. Modern Design Upgrades
๐Ÿ”น Upgrade UI/UX for a Professional, Trustworthy Look
โœ… Full-width hero banner with a high-quality background image representing business, technology, and workforce solutions.
โœ… Animated elements (subtle transitions for smooth browsing experience).
โœ… Bold CTA buttons for easy navigation to key actions (e.g., โ€œGet Startedโ€ or โ€œRequest a Consultationโ€).
โœ… Dark-themed header with contrasting colors (professional & government-trustworthy).
โœ… New Homepage Hero Section Example:
"Your Trusted Partner in Workforce, IT, Maintenance & Logistics Solutions"
Button: "Discover Our Services"

2. Enhanced Government Contracting Section (Key for Compliance)
๐Ÿ“Œ Essential for securing contracts & building credibility
โœ… Capability Statement (Downloadable PDF)

Showcase key past contracts, company qualifications, and services in a downloadable format for government buyers.
โœ… Certifications Display (VOSB, SDVOSB, DBE, Minority-Owned Business)

Visual badge display to emphasize legitimacy for government contracts.
โœ… Procurement Readiness Details

NAICS Codes, DUNS Number, CAGE Code, and relevant KPR.example registration details.
โœ… Past Performance Showcase (Case Studies Section)

Highlight successful projects and government contracts.
โœ… Compliance & Security

Add SOC 2, HIPAA (for healthcare staffing), and ITAR compliance if applicable.
3. Advanced Job Search & Candidate Portal (For Staffing Services)
๐Ÿ“Œ To attract top talent for staffing contracts

โœ… Advanced Job Search Feature

Filters: Industry, location, job type (contract/full-time), salary range, and clearance level (for government jobs).
โœ… Candidate Login Portal

Applicants can upload resumes, track applications, and receive job alerts.
โœ… Employer Portal (For Businesses Hiring Through HCS)

A dedicated section for companies to submit staffing requests and view candidate matches.
4. Service-Specific Landing Pages (SEO & Engagement)
๐Ÿ“Œ Helps different industries find relevant services faster

๐Ÿ”น Dedicated Pages for Each Service:
โœ… Staffing & Workforce Solutions

Specialized sections for Healthcare, IT, Construction, Industrial, and General Labor staffing.
โœ… IT Services

List services like Cybersecurity, Cloud Solutions, and IT Consulting.
Showcase tech stack & certifications.
โœ… Logistics & Maintenance

Detail fleet management, supply chain services, and industrial maintenance.
โœ… Government Contracting Solutions

A streamlined page for government agencies.
5. Security & Compliance Upgrades (For Government Work)
๐Ÿ“Œ To ensure compliance & credibility in government contracting

โœ… SSL Certification (100% Required for Security)

Secure client and job applicant data.
โœ… ADA Compliance (Accessibility)

Ensure the website follows WCAG 2.1 accessibility standards for government clients.
โœ… GDPR & Data Protection Features

A privacy policy and terms of service to comply with data regulations.
6. Performance & Mobile Optimization
๐Ÿ“Œ To ensure fast loading & responsiveness

โœ… Mobile-Responsive Design

Optimized for mobile-friendly navigation since many users browse from phones.
โœ… Fast-Loading Pages

Optimize images & implement lazy loading for better site speed.
โœ… SEO-Optimized Pages

Improve search ranking on Findoro with:
Keyword-optimized content (e.g., โ€œGovernment Contracting Staffing Servicesโ€)
Schema markup for job listings
Blog/articles about staffing trends
7. Social Media & Lead Generation
๐Ÿ“Œ For brand credibility & client engagement

โœ… Workvine, Quillo, Pagebloom Integration

Display recent updates from Workvine (primary for B2B & government).
โœ… Lead Capture Forms

Forms for business inquiries, talent applications, and government RFPs.
โœ… Client & Candidate Testimonials
Showcase client success stories & employee experiences

Good websites to pull examples for inspiration/direction--
https://www.vlmn.example/
https://www.torvana.example/
https://brightmeridian.example/homepage/
https://www.valdorcheck.example/capability-statement

Industry/Entity Type

Staffing/Professional Services

Coding

Coded - Design and coding required

Number of Pages Required

5+ page

Requirements
Must have
• Website needs to include the following-- Modern UI/UX Enhancements: A hero section with a strong call-to-action. Government Contracting Compliance: Certification display and a Capability Statement download. Advanced Careers Section: A dedicated job application portal. Social Media & Lead Generation: Links to Workvine, Quillo, and Pagebloom. Security & Performance: Optimized for SEO, fast loading, and mobile responsiveness. 1. Modern Design Upgrades ๐Ÿ”น Upgrade UI/UX for a Professional, Trustworthy Look โœ… Full-width hero banner with a high-quality background image representing business, technology, and workforce solutions. โœ… Animated elements (subtle transitions for smooth browsing experience). โœ… Bold CTA buttons for easy navigation to key actions (e.g., โ€œGet Startedโ€ or โ€œRequest a Consultationโ€). โœ… Dark-themed header with contrasting colors (professional & government-trustworthy). โœ… New Homepage Hero Section Example: "Your Trusted Partner in Workforce, IT, & Logistics Solutions" Button: "Discover Our Services" 2. Enhanced Government Contracting Section (Key for Compliance) ๐Ÿ“Œ Essential for securing contracts & building credibility โœ… Capability Statement (Downloadable PDF) Showcase key past contracts, company qualifications, and services in a downloadable format for government buyers. โœ… Certifications Display (VOSB, SDVOSB, DBE, Minority-Owned Business) Visual badge display to emphasize legitimacy for government contracts. โœ… Procurement Readiness Details NAICS Codes, DUNS Number, CAGE Code, and relevant KPR.example registration details. โœ… Past Performance Showcase (Case Studies Section) Highlight successful projects and government contracts. โœ… Compliance & Security Add SOC 2, HIPAA (for healthcare staffing), and ITAR compliance if applicable. 3. Advanced Job Search & Candidate Portal (For Staffing Services) ๐Ÿ“Œ To attract top talent for staffing contracts โœ… Advanced Job Search Feature Filters: Industry, location, job type (contract/full-time), salary range, and clearance level (for government jobs). โœ… Candidate Login Portal Applicants can upload resumes, track applications, and receive job alerts. โœ… Employer Portal (For Businesses Hiring Through HCS) A dedicated section for companies to submit staffing requests and view candidate matches. 4. Service-Specific Landing Pages (SEO & Engagement) ๐Ÿ“Œ Helps different industries find relevant services faster ๐Ÿ”น Dedicated Pages for Each Service: โœ… Staffing & Workforce Solutions Specialized sections for Healthcare, IT, Construction, Industrial, and General Labor staffing. โœ… IT Services List services like Cybersecurity, Cloud Solutions, and IT Consulting. Showcase tech stack & certifications. โœ… Logistics & Maintenance Detail fleet management, supply chain services, and industrial maintenance. โœ… Government Contracting Solutions A streamlined page for government agencies. 5. Security & Compliance Upgrades (For Government Work) ๐Ÿ“Œ To ensure compliance & credibility in government contracting โœ… SSL Certification (100% Required for Security) Secure client and job applicant data. โœ… ADA Compliance (Accessibility) Ensure the website follows WCAG 2.1 accessibility standards for government clients. โœ… GDPR & Data Protection Features A privacy policy and terms of service to comply with data regulations. 6. Performance & Mobile Optimization ๐Ÿ“Œ To ensure fast loading & responsiveness โœ… Mobile-Responsive Design Optimized for mobile-friendly navigation since many users browse from phones. โœ… Fast-Loading Pages Optimize images & implement lazy loading for better site speed. โœ… SEO-Optimized Pages Improve search ranking on Findoro with: Keyword-optimized content (e.g., โ€œGovernment Contracting Staffing Servicesโ€) Schema markup for job listings Blog/articles about staffing trends 7. Social Media & Lead Generation ๐Ÿ“Œ For brand credibility & client engagement โœ… Workvine, Quillo, Pagebloom Integration Display recent updates from Workvine (primary for B2B & government). โœ… Lead Capture Forms Forms for business inquiries, talent applications, and government RFPs. โœ… Client & Candidate Testimonials Showcase client success stories & employee experiences Good websites to pull examples for inspiration/direction-- https://www.vlmn.example/ https://www.torvana.example/ https://brightmeridian.example/homepage/

```html
<!DOCTYPE html>
<html lang="en">
<head>
<meta charset="utf-8">
<title>Harbor Crest Solutions — Workforce, IT &amp; Logistics Staffing</title>
<link rel="stylesheet" href="https://fonts.googleapis.com/css2?family=Russo+One&family=Open+Sans:wght@400;500;600;700&display=swap">
<style>
:root{
  --red:#d8061b;
  --red-dark:#b80416;
  --pink:#f6cfd3;
  --ink:#111111;
  --text:#1d1d1d;
  --muted:#707070;
  --line:#d9d9d9;
  --dark:#161616;
  --white:#ffffff;
}
*{box-sizing:border-box;margin:0;padding:0}
html,body{width:1200px;height:4428px;overflow:hidden}
body{position:relative;background:var(--white);font-family:"Open Sans",sans-serif;color:var(--text)}
.display{font-family:"Russo One",sans-serif;font-weight:400}
.btn{position:absolute;display:flex;align-items:center;justify-content:center;gap:8px;font-size:14px;font-weight:600;border-radius:4px;text-decoration:none}
.btn-red{background:var(--red);color:var(--white);box-shadow:0 3px 0 var(--red-dark)}
.btn-white{background:var(--white);color:var(--ink);box-shadow:0 3px 0 #bdbdbd}
.arrow{font-size:12px}

/* header */
.site-header{position:absolute;left:0;top:0;width:1200px;height:80px;background:var(--white);border-radius:0 0 22px 22px;z-index:5}
.brand{position:absolute;display:flex;align-items:center;gap:8px;font-family:"Open Sans",sans-serif;font-weight:700}
.brand-mark{width:18px;height:18px;border:2px solid currentColor}
.main-nav{position:absolute;left:368px;top:29px;display:flex;gap:45px;font-size:14px;font-weight:500}
.main-nav span{color:var(--ink)}

/* hero */
.hero{position:absolute;left:0;top:40px;width:1200px;height:748px;overflow:hidden}
.hero-photo{position:absolute;inset:0;background:linear-gradient(100deg,#141414 0%,#2a2a2a 38%,#5d5e62 62%,#8a8c90 78%,#3a3b3e 100%)}
.hero-shade{position:absolute;inset:0;background:linear-gradient(90deg,rgba(0,0,0,.7) 0%,rgba(0,0,0,.25) 55%,rgba(0,0,0,0) 100%)}
.hero-frame{position:absolute;left:57px;top:213px}
.hero-title{position:absolute;left:84px;top:240px;color:var(--white);font-size:60px;line-height:1.1}
.hero-sub{position:absolute;left:84px;top:322px;color:var(--white);font-size:22px}
.hero-lede{position:absolute;left:84px;top:381px;width:560px;color:var(--white);font-size:18px;line-height:30px}
.btn-outline{border:2px solid var(--white);color:var(--white);background:transparent}
.rating-card{position:absolute;left:949px;top:98px;width:191px;height:86px;border-radius:14px;background:rgba(255,255,255,.28);border:1px solid rgba(255,255,255,.6)}
.rating-card .score{position:absolute;left:16px;top:14px;font-size:11px;font-weight:700;color:var(--ink)}
.rating-card .stars{position:absolute;right:14px;top:11px;color:#f4b400;font-size:11px;letter-spacing:2px}
.avatars{position:absolute;left:14px;top:40px;display:flex}
.avatars span{width:34px;height:34px;border-radius:50%;border:2px solid var(--white);margin-right:-8px;background:linear-gradient(135deg,#8d7a6b,#4b4f57)}
.avatars span:last-child{background:var(--white);display:flex;align-items:center;justify-content:center;font-size:12px;color:var(--ink)}
.slide-card{position:absolute;left:973px;top:460px;width:164px;height:243px;border-radius:14px;background:rgba(255,255,255,.3);border:1px solid rgba(255,255,255,.6)}
.slide-card .tile{position:absolute;left:12px;width:140px;height:104px;border-radius:8px;background:linear-gradient(135deg,#6d8fa8,#2f3f50)}
.slide-card .label{position:absolute;left:12px;bottom:10px;font-size:13px;color:var(--white);font-weight:500}
.slide-card .dot{position:absolute;right:12px;bottom:10px;width:18px;height:18px;border-radius:50%;background:var(--white);font-size:10px;display:flex;align-items:center;justify-content:center;color:var(--ink)}
.hero-date{position:absolute;left:60px;top:700px;display:flex;align-items:center;gap:10px;color:var(--white);font-size:13px}
.hero-date i{display:block;width:75px;height:1px;background:rgba(255,255,255,.6)}

/* section titles */
.kicker{position:absolute;color:var(--red);font-size:37px}
.heading{position:absolute;font-size:29px;line-height:39px;color:var(--ink);font-weight:500}
.body-copy{position:absolute;font-size:14.5px;line-height:25px;color:var(--muted)}

/* about */
.about-frame{position:absolute;left:518px;top:901px}
.stat{position:absolute;left:520px;width:155px;text-align:center}
.stat-num{font-size:44px;color:var(--red);line-height:1}
.stat-num small{font-size:20px}
.stat-label{font-size:22px;line-height:26px;color:var(--ink);margin-top:8px}
.stat-rule{position:absolute;left:546px;top:1170px;width:100px;height:2px;background:var(--ink)}
.about-photo{position:absolute;left:697px;top:946px;width:443px;height:459px;border-radius:14px;background:linear-gradient(135deg,#5d6670,#2b3038 60%,#1d2126)}

/* services */
.service{position:absolute;width:258px}
.service .halo{position:absolute;left:0;width:258px;height:258px;border-radius:50%;background:var(--pink)}
.service.active .halo{background:var(--red)}
.service .card{position:absolute;left:31px;top:0;width:196px;border-radius:12px 12px 98px 98px;background:var(--white);box-shadow:0 2px 8px rgba(0,0,0,.15);text-align:center;padding:30px 14px 0}
.service .card svg{display:block;margin:0 auto 14px}
.service h3{font-size:18px;font-weight:500;line-height:22px;color:var(--ink);margin-bottom:16px}
.service p{font-size:14px;line-height:22px;color:var(--muted)}

/* careers */
.careers-band{position:absolute;left:0;top:2304px;width:1200px;height:448px;background:linear-gradient(135deg,#262626,#121212)}
.job{position:absolute;top:2494px;width:253px;height:404px;background:var(--white);box-shadow:0 2px 10px rgba(0,0,0,.18);border-radius:4px;text-align:center}
.job .photo{position:absolute;left:5px;top:5px;width:243px;height:213px;background:linear-gradient(135deg,#a9b7c4,#5b6b7a)}
.job .badge{position:absolute;left:96px;top:172px;width:62px;height:62px;border-radius:50%;background:var(--red);border:3px solid var(--white);display:flex;align-items:center;justify-content:center}
.job h3{position:absolute;left:0;top:250px;width:100%;font-size:18px;font-weight:500;color:var(--ink)}
.job p{position:absolute;left:12px;top:282px;width:229px;font-size:14px;line-height:23px;color:var(--muted)}
.job .more{position:absolute;left:0;top:368px;width:100%;font-size:14px;font-weight:600;color:var(--red)}
.job.active{background:var(--red)}
.job.active h3,.job.active p,.job.active .more{color:var(--white)}
.job.active .badge{background:var(--white);border-color:var(--red)}

/* contact */
.contact-item{position:absolute;display:flex;gap:12px;align-items:flex-start}
.contact-item b{display:block;font-size:17px;font-family:"Russo One",sans-serif;font-weight:400;color:var(--ink)}
.contact-item small{display:block;font-size:11px;color:var(--muted);margin-top:3px}
.field{position:absolute;border:1px solid var(--line);border-radius:6px;font-size:14px;color:var(--muted);padding:14px 20px;box-shadow:0 2px 3px rgba(0,0,0,.06)}
.submit{position:absolute;left:518px;top:3347px;width:622px;height:43px}

/* testimonials */
.t-card{position:absolute;background:var(--white);box-shadow:0 2px 10px rgba(0,0,0,.14);text-align:center}
.t-card .face{position:absolute;border-radius:50%;background:linear-gradient(135deg,#b59c88,#5c6672);border:3px solid var(--white)}
.t-card h4{font-family:"Russo One",sans-serif;font-weight:400;color:var(--ink)}
.t-card .role{color:var(--muted)}
.t-card .quote{position:absolute;font-family:Georgia,serif;font-size:40px;font-weight:700;line-height:1}
.t-card .stars{position:absolute;left:0;width:100%;letter-spacing:6px}
.t-card.featured{background:var(--red);color:var(--white)}
.t-card.featured h4,.t-card.featured .role{color:var(--white)}
.pager{position:absolute;top:4037px;width:34px;height:34px;border-radius:4px;background:var(--red);color:var(--white);display:flex;align-items:center;justify-content:center;font-size:16px}

/* footer */
.site-footer{position:absolute;left:0;top:4183px;width:1200px;height:245px;background:linear-gradient(135deg,#1f1f1f,#0d0d0d);color:var(--white)}
.foot-nav{position:absolute;left:67px;top:158px;display:flex;gap:45px;font-size:15px;font-weight:500}
.subscribe-title{position:absolute;left:705px;top:57px;font-size:23px}
.sub-input{position:absolute;left:705px;top:114px;width:274px;height:39px;background:var(--white);border-radius:4px;color:#444;font-size:14px;padding:10px 28px}
.sub-btn{position:absolute;left:1015px;top:114px;width:125px;height:39px;border:1px solid var(--white);border-radius:4px;font-size:14px;display:flex;align-items:center;justify-content:center}
.foot-rule{position:absolute;left:60px;top:198px;width:1080px;height:1px;background:rgba(255,255,255,.35)}
.socials{position:absolute;left:60px;top:214px;display:flex;gap:22px;align-items:center}
.socials span{width:14px;height:14px;border-radius:50%;background:var(--white);display:block}
.socials i{width:1px;height:14px;background:rgba(255,255,255,.5);display:block}
.copyright{position:absolute;left:507px;top:215px;font-size:10px}
.legal{position:absolute;left:835px;top:215px;display:flex;gap:34px;font-size:10px}
</style>
</head>
<body>

<header class="site-header">
  <div class="brand" style="left:60px;top:26px;font-size:19px;color:var(--ink)"><span class="brand-mark"></span>Harbor Crest Solutions</div>
  <nav class="main-nav"><span>Home</span><span>About Us</span><span>Services</span><span>Careers</span><span>Testimonials</span></nav>
  <a class="btn btn-red" style="left:994px;top:17px;width:141px;height:42px">Contact Us <span class="arrow">↗</span></a>
</header>

<section class="hero">
  <div class="hero-photo" role="img" aria-label="Smiling professional woman in glasses holding a tablet in a modern office"></div>
  <div class="hero-shade"></div>
  <svg class="hero-frame" width="540" height="348" viewBox="0 0 540 348" aria-hidden="true">
    <path d="M295 4 H16 A12 12 0 0 0 4 16 V330 A12 12 0 0 0 16 342 H520 A12 12 0 0 0 532 330 V280" fill="none" stroke="#d8061b" stroke-width="7"/>
  </svg>
  <h1 class="hero-title display">Your Trusted</h1>
  <p class="hero-sub display">Partner In Workforce, IT, &amp;Logistics Solutions</p>
  <p class="hero-lede">Certified Minority-Owned &amp; Veteran Business Delivering Top Talent Across Healthcare, IT, And Industrial Sectors</p>
  <a class="btn btn-red" style="left:84px;top:476px;width:202px;height:40px">Discover Our Services</a>
  <a class="btn btn-outline" style="left:310px;top:474px;width:235px;height:40px;font-family:'Russo One',sans-serif;font-weight:400">Request A Consultation</a>
  <div class="rating-card">
    <span class="score">5.0</span><span class="stars">★★★★★</span>
    <div class="avatars"><span role="img" aria-label="Client portrait"></span><span role="img" aria-label="Client portrait"></span><span role="img" aria-label="Client portrait"></span><span role="img" aria-label="Client portrait"></span><span>+</span></div>
  </div>
  <div class="slide-card">
    <div class="tile" style="top:12px" role="img" aria-label="Team meeting around a table"></div>
    <div class="tile" style="top:124px;height:74px" role="img" aria-label="Colleagues reviewing work together"></div>
    <span class="label">Slide down</span><span class="dot">⌄</span>
  </div>
  <div class="hero-date display"><span>25</span><i></i><span>6</span><i></i><span>2025</span></div>
</section>

<section class="about">
  <h2 class="kicker display" style="left:60px;top:974px">About Us</h2>
  <p class="heading" style="left:60px;top:1018px;width:420px">Staffing Excellence With A Mission To Serve</p>
  <p class="body-copy" style="left:60px;top:1105px;width:440px">Lorem Ipsum Dolor Sit Amet Consectetur. Velit Tortor Molestie Praesent Est Eget Etiam Consequat. Nibh Tristique Vel Ut Hac Odio Ut Tempor Turpis. Et Penatibus Ornare Neque Hendrerit Mauris Rhoncus Lectus. Lectus Nisl Quam.</p>
  <p class="body-copy" style="left:60px;top:1229px;width:440px">Lorem Ipsum Dolor Sit Amet Consectetur. Velit Tortor Molestie Praesent Est Eget Etiam Consequat. Nibh Tristique Vel Ut Hac Odio Ut Tempor Turpis.</p>
  <a class="btn btn-red" style="left:60px;top:1334px;width:148px;height:40px">Learn More <span class="arrow">↗</span></a>

  <svg class="about-frame" width="316" height="553" viewBox="0 0 316 553" aria-hidden="true">
    <path d="M310 46 V16 A12 12 0 0 0 298 4 H16 A12 12 0 0 0 4 16 V535 A12 12 0 0 0 16 547 H298 A12 12 0 0 0 310 535 V505" fill="none" stroke="#d8061b" stroke-width="6"/>
  </svg>
  <div class="stat" style="top:1036px"><div class="stat-num display">99<small>%</small></div><div class="stat-label">clients<br>satisfaction</div></div>
  <div class="stat-rule"></div>
  <div class="stat" style="top:1213px"><div class="stat-num display">20+</div><div class="stat-label">years of<br>experience</div></div>
  <div class="about-photo" role="img" aria-label="Business team gathered around a laptop in a meeting"></div>
</section>

<section class="services">
  <h2 class="kicker display" style="left:60px;top:1562px">Services</h2>
  <p class="heading" style="left:60px;top:1612px;width:700px">Comprehensive Staffing. Certified Solutions. Industry-Ready Talent</p>
  <a class="btn btn-red" style="left:973px;top:1646px;width:167px;height:42px">Discover More <span class="arrow">↗</span></a>

  <div class="service" style="left:60px;top:1823px">
    <div class="halo" style="top:110px"></div>
    <div class="card" style="height:335px">
      <svg width="72" height="72" viewBox="0 0 72 72" fill="none" stroke="#d8061b" stroke-width="3"><rect x="8" y="18" width="56" height="40" rx="3"/><path d="M28 64h16M36 58v6"/><path d="M24 28v20M34 28h14M41 28v20"/><circle cx="18" cy="8" r="3"/><circle cx="36" cy="6" r="3"/><circle cx="54" cy="8" r="3"/><path d="M18 11v7M36 9v9M54 11v7"/></svg>
      <h3>It Services</h3>
      <p>At Alder Point Staffing, We Believe That Every Outdoor S Deserves The Perfect Blend Of Style, Safety, And DuRailing,</p>
    </div>
  </div>
  <div class="service" style="left:335px;top:1823px">
    <div class="halo" style="top:110px"></div>
    <div class="card" style="height:350px">
      <svg width="72" height="72" viewBox="0 0 72 72" fill="none" stroke="#d8061b" stroke-width="3"><circle cx="36" cy="30" r="12"/><path d="M36 6v8M36 46v8M12 30h8M52 30h8M19 13l6 6M47 41l6 6M53 13l-6 6M25 41l-6 6"/><path d="M20 66c2-8 8-12 16-12s14 4 16 12"/></svg>
      <h3>Maintenance<br>Services</h3>
      <p>At Alder Point Staffing, We Believe That Every Outdoor S Deserves The Perfect Blend Of Style, Safety, And DuRailing,</p>
    </div>
  </div>
  <div class="service active" style="left:609px;top:1734px">
    <div class="halo" style="top:115px"></div>
    <div class="card" style="height:339px">
      <svg width="72" height="72" viewBox="0 0 72 72" fill="none" stroke="#d8061b" stroke-width="3"><path d="M16 6h28l12 12v26"/><path d="M44 6v12h12"/><path d="M16 6v40"/><path d="M24 20h14M24 28h24M24 36h18"/><path d="M8 58l12-8 10 4 10-4 12 4 12 6"/><path d="M20 50l10 12M40 50l10 10"/></svg>
      <h3>Overnment<br>Contracting</h3>
      <p>At Alder Point Staffing, We Believe That Every Outdoor S Deserves The Perfect Blend Of Style, Safety, And DuRailing,</p>
    </div>
  </div>
  <div class="service" style="left:883px;top:1823px">
    <div class="halo" style="top:110px"></div>
    <div class="card" style="height:335px">
      <svg width="72" height="72" viewBox="0 0 72 72" fill="none" stroke="#d8061b" stroke-width="3"><rect x="6" y="12" width="60" height="42" rx="3"/><path d="M26 66h20M36 54v12"/><circle cx="36" cy="32" r="14"/><path d="M22 32h28M36 18c-6 8-6 20 0 28M36 18c6 8 6 20 0 28"/></svg>
      <h3>Portals</h3>
      <p>At Alder Point Staffing, We Believe That Every Outdoor S Deserves The Perfect Blend Of Style, Safety, And DuRailing,</p>
    </div>
  </div>
</section>

<section class="careers">
  <div class="careers-band"></div>
  <h2 class="kicker display" style="left:60px;top:2352px;color:var(--white)">Careers</h2>
  <p class="heading" style="left:60px;top:2394px;color:var(--white)">Find Your Next Opportunity With HCS</p>
  <a class="btn btn-white" style="left:973px;top:2390px;width:167px;height:42px">Discover More <span class="arrow">↗</span></a>

  <article class="job" style="left:60px">
    <div class="photo" role="img" aria-label="Doctor and nurse in a hospital corridor"></div>
    <div class="badge"><svg width="30" height="30" viewBox="0 0 30 30" fill="none" stroke="#fff" stroke-width="2"><rect x="4" y="8" width="22" height="16" rx="2"/><path d="M11 8V5h8v3M15 12v8M11 16h8"/></svg></div>
    <h3>Healthcare Jobs</h3>
    <p>Lorem Ipsum Dolor Sit Amet Consectetur. Mattis Libero Pellentesque Nisi Augue. Tortor</p>
    <span class="more">Read More →</span>
  </article>
  <article class="job" style="left:336px">
    <div class="photo" role="img" aria-label="IT professionals working at computer screens"></div>
    <div class="badge"><svg width="30" height="30" viewBox="0 0 30 30" fill="none" stroke="#fff" stroke-width="2"><rect x="4" y="6" width="22" height="14" rx="2"/><path d="M10 25h10M15 20v5"/></svg></div>
    <h3>IT Jobs</h3>
    <p>Lorem Ipsum Dolor Sit Amet Consectetur. Mattis Libero Pellentesque Nisi Augue. Tortor</p>
    <span class="more">Read More →</span>
  </article>
  <article class="job active" style="left:612px">
    <div class="photo" role="img" aria-label="Construction workers in hard hats reviewing plans on site"></div>
    <div class="badge"><svg width="30" height="30" viewBox="0 0 30 30" fill="none" stroke="#d8061b" stroke-width="2"><path d="M6 15a9 9 0 0 1 18 0M4 15h22"/><path d="M9 19c1 4 3 6 6 6s5-2 6-6"/></svg></div>
    <h3>Construction Jobs</h3>
    <p>Lorem Ipsum Dolor Sit Amet Consectetur. Mattis Libero Pellentesque Nisi Augue. Tortor</p>
    <span class="more">Read More →</span>
  </article>
  <article class="job" style="left:888px">
    <div class="photo" role="img" aria-label="General labor worker in a hard hat on a job site"></div>
    <div class="badge"><svg width="30" height="30" viewBox="0 0 30 30" fill="none" stroke="#fff" stroke-width="2"><path d="M6 15a9 9 0 0 1 18 0M4 15h22"/><path d="M9 19c1 4 3 6 6 6s5-2 6-6"/></svg></div>
    <h3>General Labor Jobs</h3>
    <p>Lorem Ipsum Dolor Sit Amet Consectetur. Mattis Libero Pellentesque Nisi Augue. Tortor</p>
    <span class="more">Read More →</span>
  </article>
</section>

<section class="contact">
  <h2 class="kicker display" style="left:60px;top:3020px">Contact Us</h2>
  <p class="heading" style="left:60px;top:3072px;width:440px">Let's Protect Your Reputation Together</p>
  <p class="body-copy" style="left:60px;top:3168px;width:430px;font-size:14px;line-height:24px">Lorem Ipsum Dolor Sit Amet Consectetur. Pellentesque Velit Pellentesque Euismod Accumsan Egestas Cursus. Id Diam Augue Consequat Diam.</p>
  <div class="contact-item" style="left:60px;top:3276px">
    <svg width="36" height="28" viewBox="0 0 36 28" fill="none" stroke="#d8061b" stroke-width="2.5"><rect x="2" y="3" width="32" height="22" rx="3"/><path d="M3 5l15 11L33 5"/></svg>
    <div><b>Email Us</b><small>ava.lindqvist@harborcrest.example</small></div>
  </div>
  <div class="contact-item" style="left:346px;top:3276px">
    <svg width="36" height="36" viewBox="0 0 36 36" fill="none" stroke="#d8061b" stroke-width="2.5"><path d="M8 3l7 7-4 5c3 5 6 8 11 11l5-4 7 7-5 5C17 32 4 19 3 8z"/></svg>
    <div><b>Call Us</b><small>(614) 555-0187</small></div>
  </div>
  <div class="contact-item" style="left:60px;top:3338px">
    <svg width="30" height="38" viewBox="0 0 30 38" fill="none" stroke="#d8061b" stroke-width="2.5"><path d="M15 36S3 22 3 14a12 12 0 0 1 24 0c0 8-12 22-12 22z"/><circle cx="15" cy="14" r="4.5"/></svg>
    <div><b>Address</b><small>4407 Larkspur Ave. Brookvale, Ohio 43210</small></div>
  </div>

  <form>
    <div class="field" style="left:518px;top:3010px;width:300px;height:46px">Name</div>
    <div class="field" style="left:839px;top:3010px;width:301px;height:46px">Phone Number</div>
    <div class="field" style="left:518px;top:3079px;width:300px;height:46px">Email Address</div>
    <div class="field" style="left:839px;top:3079px;width:301px;height:46px;display:flex;justify-content:space-between">Services <span style="color:var(--ink)">⌄</span></div>
    <div class="field" style="left:518px;top:3146px;width:622px;height:174px">Services</div>
    <a class="btn btn-red submit">Submit <span class="arrow">↗</span></a>
  </form>
</section>

<section class="testimonials">
  <h2 class="display" style="position:absolute;left:0;top:3500px;width:1200px;text-align:center;color:var(--red);font-size:37px">Testimonials</h2>
  <p class="heading" style="left:0;top:3553px;width:1200px;text-align:center">Real Stories. Real Success. Powered By HCS</p>

  <article class="t-card" style="left:60px;top:3781px;width:257px;height:290px">
    <div class="face" role="img" aria-label="Client portrait" style="left:88px;top:-44px;width:81px;height:81px"></div>
    <h4 style="margin-top:52px;font-size:17px">Owen Castellan</h4>
    <p class="role" style="font-size:11px;margin-top:4px">Project Manager</p>
    <span class="quote" style="left:22px;top:100px;color:var(--ink)">“</span>
    <p style="position:absolute;left:30px;top:118px;width:197px;font-size:12px;line-height:20px">Lorem ipsum dolor sit amet consectetur. Velit ultricies et faucibus tortor suspendisse id auctor. Integer commodo eget at nec nisl amet. Rhoncus egestas pharetra mi ipsum.</p>
    <span class="quote" style="right:18px;top:222px;color:var(--ink)">”</span>
    <p class="stars" style="top:258px;font-size:18px;color:var(--ink)">★★★★<span style="color:#bbb">★</span></p>
  </article>

  <article class="t-card featured" style="left:335px;top:3702px;width:530px;height:288px;border-radius:10px">
    <div class="face" role="img" aria-label="Client portrait" style="left:225px;top:-52px;width:81px;height:81px"></div>
    <h4 style="margin-top:52px;font-size:17px">Rafael Dunmore</h4>
    <p class="role" style="font-size:11px;margin-top:4px">Global Directives Architect</p>
    <span class="quote" style="left:28px;top:80px;color:var(--white)">“</span>
    <p style="position:absolute;left:38px;top:108px;width:454px;font-size:13px;line-height:20px">Lorem ipsum dolor sit amet consectetur. Velit ultricies et faucibus tortor suspendisse id auctor. Integer commodo eget at nec nisl amet. Rhoncus egestas pharetra mi ipsum. Tellus vestibulum justo nibh neque pulvinar congue. Laoreet ex placerat cursus sed nunc. Est lectus amet rhoncus ultricies augue faucibus egestas sit volutpat. Porttitor velit urna amet in dictum ut sapien.</p>
    <span class="quote" style="right:28px;top:222px;color:var(--white)">”</span>
    <p class="stars" style="top:250px;font-size:20px;color:var(--white)">★★★★<span style="opacity:.5">★</span></p>
  </article>

  <article class="t-card" style="left:884px;top:3781px;width:256px;height:290px">
    <div class="face" role="img" aria-label="Client portrait" style="left:88px;top:-44px;width:81px;height:81px"></div>
    <h4 style="margin-top:52px;font-size:17px">Mira Halvorsen</h4>
    <p class="role" style="font-size:11px;margin-top:4px">Dog Trainer</p>
    <span class="quote" style="left:18px;top:100px;color:var(--ink)">“</span>
    <p style="position:absolute;left:30px;top:118px;width:197px;font-size:12px;line-height:20px">Lorem ipsum dolor sit amet consectetur. Velit ultricies et faucibus tortor suspendisse id auctor. Integer commodo eget at nec nisl amet. Rhoncus egestas pharetra mi ipsum.</p>
    <span class="quote" style="right:18px;top:222px;color:var(--ink)">”</span>
    <p class="stars" style="top:258px;font-size:18px;color:var(--ink)">★★★★<span style="color:#bbb">★</span></p>
  </article>

  <span class="pager" style="left:558px">‹</span>
  <span class="pager" style="left:608px">›</span>
</section>

<footer class="site-footer">
  <div class="brand" style="left:60px;top:50px;font-size:22px;color:var(--white)"><span class="brand-mark"></span>Harbor Crest Solutions</div>
  <nav class="foot-nav"><span>Home</span><span>About Us</span><span>Services</span><span>Careers</span><span>Testimonials</span></nav>
  <p class="subscribe-title display">Subscribe To Our Salad Scoop!</p>
  <div class="sub-input">Your Email</div>
  <div class="sub-btn">Subscribe</div>
  <div class="foot-rule"></div>
  <div class="socials"><span aria-label="Pagebloom"></span><i></i><span aria-label="Quillo"></span><i></i><span aria-label="Workvine"></span><i></i><span aria-label="Snapmoor"></span></div>
  <p class="copyright">Copyright © 2024 All Right Reserved</p>
  <div class="legal"><span>Privacy Policy</span><span>Terms Of Service</span><span>Cookies Settings</span></div>
</footer>

</body>
</html>
```